販促の一環として、「初回限定無料お試しキャンペーン」を行います。

つきましてはトップバナーx1枚(960 x 500)※若干変更の可能性あり
ピコルン広告用バナー x1枚
計2枚の制作をお願い致します。

※ピコルン広告用バナーには添付の弊社ロゴも入れて頂ければ助かります。
(必須ではなくデザイン的に入れない方が良い場合は外して頂いて問題ありません。)

【添付】
なんとなく気に入ったものを無作為に載せました。
(ご参考として。)
・初回限定無料お試しキャンペーン
(上記内容が伝われば表記は問いません。)
・期間:2022/7/31まで
• 960x500

シンプルながらも細部まで手の込んだデザインが大変気に入りました。

この度は素晴らしいご提案を多数頂き、誠にありがとうございました。
今後もバナー制作をコンペ形式でお願いすることがございますので、
その際はご応募頂けますと幸いです。

```html
<!DOCTYPE html>
<html lang="ja">
<head>
<meta charset="UTF-8">
<title>初回限定 無料お試しキャンペーン バナー</title>
<link href="https://fonts.googleapis.com/css2?family=M+PLUS+Rounded+1c:wght@700;800;900&display=swap" rel="stylesheet">
<style>
  :root {
    --yellow: #ffe94a;
    --yellow-light: #fff8b8;
    --pink: #ef5a86;
    --pink-dark: #d8406d;
    --green: #3fb54c;
    --green-dark: #23893a;
    --hill: #4cbf57;
    --hill-light: #6fd277;
    --white: #ffffff;
    --gap: #ffffff;
  }
  * { margin: 0; padding: 0; box-sizing: border-box; }
  html, body { width: 773px; height: 1200px; overflow: hidden; background: var(--gap); }
  body { font-family: "M PLUS Rounded 1c", sans-serif; position: relative; }

  .banner { position: absolute; left: 0; width: 773px; overflow: hidden; }
  .banner--top { top: 0; height: 372px; }
  .banner--ad { top: 388px; height: 812px; }

  .burst {
    position: absolute; inset: 0;
    background: radial-gradient(ellipse at 50% 45%, var(--yellow-light) 0%, var(--yellow) 55%, #ffe03a 100%);
  }
  .hill { position: absolute; left: 0; width: 100%; }

  .centered { position: absolute; left: 0; width: 100%; text-align: center; }

  .category { color: var(--pink); font-weight: 900; letter-spacing: 0.08em; }

  .limited {
    position: absolute; left: 50%; transform: translateX(-50%);
    background: var(--white); border: 5px solid var(--pink); border-radius: 10px;
    color: var(--pink); font-weight: 900; text-align: center; letter-spacing: 0.06em;
    box-shadow: 5px 5px 0 var(--pink-dark);
  }

  .headline {
    color: var(--green); font-weight: 900; line-height: 1;
    -webkit-text-stroke: 10px var(--white); paint-order: stroke fill;
    text-shadow: 4px 5px 0 var(--green-dark);
    transform: rotate(-3deg);
  }

  .ribbon {
    position: absolute; left: 50%; transform: translateX(-50%);
    color: var(--white); font-weight: 800; text-align: center;
  }
  .ribbon svg { position: absolute; inset: 0; width: 100%; height: 100%; }
  .ribbon span { position: relative; }

  .brand { position: absolute; left: 0; width: 100%; text-align: center; color: var(--green-dark); font-weight: 900; }
  .brand__mark { display: inline-block; width: 26px; height: 26px; border-radius: 50%; background: var(--green-dark); vertical-align: -3px; margin-right: 10px; }
  .brand__sub { display: block; font-size: 16px; font-weight: 900; letter-spacing: 0.1em; margin-top: 2px; }
</style>
</head>
<body>

<section class="banner banner--top">
  <div class="burst" role="img" aria-label="放射状の光線と紙吹雪の背景"></div>
  <svg class="hill" style="top:270px;height:102px" viewBox="0 0 773 102" preserveAspectRatio="none">
    <path d="M0 40 Q386 -20 773 40 L773 102 L0 102 Z" fill="var(--hill)"/>
  </svg>
  <p class="centered category" style="top:20px;font-size:28px;">レディースゴルフウェア</p>
  <p class="limited" style="top:66px;width:270px;height:62px;font-size:40px;line-height:52px;">初回限定</p>
  <p class="centered headline" style="top:158px;font-size:62px;">無料お試しキャンペーン</p>
  <div class="ribbon" style="top:300px;width:300px;height:40px;font-size:19px;line-height:40px;">
    <svg viewBox="0 0 300 40" preserveAspectRatio="none"><path d="M0 4 L300 4 L288 20 L300 36 L0 36 L12 20 Z" fill="var(--pink)"/></svg>
    <span>2022年7月31日まで</span>
  </div>
</section>

<section class="banner banner--ad">
  <div class="burst" role="img" aria-label="放射状の光線と紙吹雪の背景"></div>
  <svg class="hill" style="top:540px;height:272px" viewBox="0 0 773 272" preserveAspectRatio="none">
    <path d="M0 60 Q386 -30 773 60 L773 272 L0 272 Z" fill="var(--hill)"/>
  </svg>
  <div class="brand" style="top:50px;font-size:40px;line-height:1;">
    <span class="brand__mark"></span>TEE PLUS
    <span class="brand__sub">-ティープラス-</span>
  </div>
  <p class="centered category" style="top:126px;font-size:36px;">レディースゴルフウェア</p>
  <p class="limited" style="top:184px;width:336px;height:96px;font-size:68px;line-height:84px;">初回限定</p>
  <p class="centered headline" style="top:310px;font-size:88px;">無料お試し</p>
  <p class="centered headline" style="top:414px;font-size:112px;letter-spacing:-0.02em;">キャンペーン</p>
  <div class="ribbon" style="top:602px;width:420px;height:76px;font-size:36px;line-height:76px;">
    <svg viewBox="0 0 420 76" preserveAspectRatio="none"><path d="M0 8 L420 8 L400 38 L420 68 L0 68 L20 38 Z" fill="var(--pink)"/></svg>
    <span>2022年7月31日まで</span>
  </div>
</section>

</body>
</html>
```